Square Business Cards for Our Restaurant / Event Venue

We need square business cards designed for the management team of our event venue and restaurant. On one side of the card should be the the Harbor Lantern 7 logo and URL www.harborlantern7.example. On the other side should be the Ember Logo and URL www.emberhall7.example. All employee details should be on the side with Ember logo. There will be a total of 5 cards to be created with the design.

Clara Bennquist
clara@harborlantern7.example

main 555.418.3072
direct 555.730.2946

4831 West Orchard Lane SE
Washington, DC 90417

Industry/Entity Type

Business

```html
<!DOCTYPE html>
<html lang="en">
<head>
<meta charset="utf-8">
<title>Ember &amp; Harbor Lantern 7 — Square Business Cards</title>
<link rel="stylesheet" href="https://fonts.googleapis.com/css2?family=Questrial&display=swap">
<style>
  :root {
    --backdrop: #ecebea;
    --ember-red: #8e1016;
    --ember-red-light: #c8141c;
    --ember-red-deep: #a30d14;
    --ink-black: #141213;
    --card-black: #1a1718;
    --circle-red: #b81e22;
    --text-white: #ffffff;
    --url-red: #c4161c;
  }
  * { margin: 0; padding: 0; box-sizing: border-box; }
  html, body {
    width: 1200px;
    height: 800px;
    overflow: hidden;
    background: var(--backdrop);
    font-family: "Questrial", "Century Gothic", sans-serif;
  }
  .canvas {
    position: relative;
    width: 1200px;
    height: 800px;
  }
  .card {
    position: absolute;
    top: 180px;
    width: 440px;
    height: 440px;
    box-shadow: 0 10px 28px rgba(0,0,0,0.22);
    overflow: hidden;
  }

  /* Ember side: staff details */
  .card--ember {
    left: 120px;
    background: var(--ember-red);
  }
  .ember-facets {
    position: absolute;
    top: 0;
    right: 0;
    width: 300px;
    height: 280px;
    background: linear-gradient(215deg, var(--ember-red-light) 0%, var(--ember-red-deep) 55%, rgba(142,16,22,0) 100%);
  }
  .ember-name {
    position: absolute;
    top: 58px;
    left: 48px;
    font-size: 64px;
    color: var(--ink-black);
    letter-spacing: 1px;
    line-height: 1;
  }
  .staff-details {
    position: absolute;
    left: 48px;
    top: 210px;
    color: var(--text-white);
  }
  .staff-name {
    font-size: 22px;
    margin-bottom: 8px;
  }
  .staff-line {
    font-size: 14px;
    line-height: 1.55;
  }
  .staff-line .label-sep { margin-right: 4px; font-size: 16px; }
  .staff-address { margin-top: 10px; }
  .staff-web {
    margin-top: 18px;
    font-size: 15px;
  }

  /* Harbor Lantern 7 side: brand */
  .card--harbor {
    left: 640px;
    background: var(--card-black);
  }
  .harbor-mark {
    position: absolute;
    top: 60px;
    left: 80px;
    width: 280px;
    height: 280px;
    border-radius: 50%;
    background: var(--circle-red);
    display: flex;
    align-items: center;
    justify-content: center;
  }
  .harbor-name {
    font-size: 34px;
    color: var(--ink-black);
    text-align: center;
    line-height: 1.15;
  }
  .harbor-web {
    position: absolute;
    left: 0;
    right: 0;
    bottom: 52px;
    text-align: center;
    font-size: 17px;
    color: var(--url-red);
    letter-spacing: 0.5px;
  }
</style>
</head>
<body>
  <main class="canvas">
    <section class="card card--ember" aria-label="Ember staff card">
      <div class="ember-facets" role="img" aria-label="Angular red facet shapes decorating the corner"></div>
      <div class="ember-name">Ember</div>
      <div class="staff-details">
        <p class="staff-name">Clara Bennquist</p>
        <p class="staff-line">clara@harborlantern7.example</p>
        <p class="staff-line"><span class="label-sep">p |</span>main 555.418.3072</p>
        <p class="staff-line">direct 555.730.2946</p>
        <p class="staff-line staff-address">4831 West Orchard Lane SE</p>
        <p class="staff-line">Washington, DC 90417</p>
        <p class="staff-web">www.emberhall7.example</p>
      </div>
    </section>

    <section class="card card--harbor" aria-label="Harbor Lantern 7 brand card">
      <div class="harbor-mark">
        <p class="harbor-name">Harbor<br>Lantern 7</p>
      </div>
      <p class="harbor-web">www.harborlantern7.example</p>
    </section>
  </main>
</body>
</html>
```